Brand New Product Needs Sales Focused Website Design

Looking for design of Homepage, Category Page & Product Page for single product sales focused website. TrendaCrate manufacture and distribute a brand new product to the market called FoldiPal-Crate which is a super strong, re-useable, folding & stacking plastic box which can be seen on our current website www.foldipal-crate.example FoldiPal-Crate was originally developed as an alternative to supermarket carrier bags and was pitched as a box for life against the other low end re-useable products. The original version was made from recycled plastic and pitched very much as environmental product. We are now taking a different direction and have re-designed the boxes in 5 bright and fashionable designs and although we still want the primary focus to be supermarket shopping we want to position the product as a design led, must have shopping and household accessory rather than a boring, cheap looking black plastic box. The new designs will still have the environmental benefits of being able to be re-used thousands of times and being 100% recyclable and save on the imminent 5p tax on carrier bags in the UK however the new designs will not be made from recycled material. Although the main use for FoldiPal-Crate is supermarket shopping it has a multitude of other uses especially where you need temporary storage - laundry, back of the car, moving house/students, gardening, days out, home office filing (will take A4 file), recycling and much more - FoldiPal-Crate is made out of super strong Polypropylene and can be easily washed and sanitised after use and can be folded and unfolded thousands of times and so will last for many years. FoldiPal-Crate is a product that needs to be seen in action to be understood so the web design must quickly and easily communicate what FoldiPal-Crate is and how it works - this can be done with video, images and copy. Our current website does not work for many reasons:- it is too busy, has too much information, tries too hard and ultimately isn't working. Any of the images off our current website can be supplied for use. Once the concept of the website is agreed I can get these photoshopped with the new designs. Pictures of new designs for reference will be attached to this brief. Ultimately we want the website to convert visitors to sales and therefore designers with a proven track record in this field are especially welcome to enter. We also have a Fileharbor folder with over 100 product and situation images in - please send email address and we will send an invite to the folder. Due to Christmas period this competition will be run over 15 days however we may choose to extend the deadline to account for the non working days. Any questions feel free to ask - we will respond within 24 hours where possible.

```html
<!DOCTYPE html>
<html lang="en">
<head>
<meta charset="utf-8">
<title>FoldiPal-Crate – Storage Boxes</title>
<link rel="stylesheet" href="https://fonts.googleapis.com/css2?family=Ubuntu:ital,wght@0,300;0,400;0,500;0,700;1,300;1,400;1,700&display=swap">
<style>
  :root {
    --cyan: #1cb5ea;
    --cyan-light: #3fc0ef;
    --grey-text: #555;
    --grey-icon: #8a8a8a;
    --grey-line: #dcdcdc;
    --tab-grey: #9b9b9b;
    --hero-top: #f4f4f4;
    --hero-bottom: #e6e6e6;
    --white: #fff;
    --brand-grey: #5a5a5a;
  }
  * { box-sizing: border-box; margin: 0; padding: 0; }
  html, body { width: 1067px; height: 1200px; overflow: hidden; }
  body { font-family: "Ubuntu", sans-serif; color: var(--grey-text); background: var(--white); position: relative; }
  ul { list-style: none; }

  .hero {
    position: absolute; left: 0; top: 0; width: 1067px; height: 643px;
    background: radial-gradient(ellipse at 50% 35%, #fbfbfb 0%, var(--hero-top) 45%, var(--hero-bottom) 100%);
  }
  .brand {
    position: absolute; display: flex; align-items: center; gap: 10px;
    font-family: "Ubuntu", sans-serif; font-weight: 700; color: var(--brand-grey);
    white-space: nowrap;
  }
  .brand-name { line-height: 1.05; }
  .brand-mark { background: var(--brand-grey); flex: none; }
  .hero .brand { left: 40px; top: 48px; font-size: 32px; }
  .hero .brand-mark { width: 22px; height: 22px; }

  .tagline {
    position: absolute; left: 269px; top: 56px; width: 606px; height: 53px;
    background: rgba(255,255,255,0.75);
    font-style: italic; font-weight: 300; font-size: 25px; color: var(--cyan-light);
    display: flex; align-items: center; justify-content: center; white-space: nowrap;
  }
  .tagline strong { font-weight: 700; margin-left: 7px; }

  .product-photo {
    position: absolute; left: 380px; top: 127px; width: 380px; height: 300px;
    background: linear-gradient(180deg, #c9b89a 0%, #9fb36a 25%, #2f6fb3 45%, #2a64a8 100%);
    border-radius: 4px;
  }
  .product-shadow {
    position: absolute; left: 300px; top: 375px; width: 470px; height: 70px;
    background: radial-gradient(ellipse, rgba(0,0,0,0.12), rgba(0,0,0,0) 70%);
  }
  .chevron { position: absolute; }

  .features {
    position: absolute; left: 0; top: 520px; width: 1067px; height: 107px; display: flex;
  }
  .feature {
    flex: 1; display: flex; flex-direction: column; align-items: center; justify-content: space-between;
    padding: 10px 0 12px; font-size: 17px; color: var(--grey-text);
  }
  .feature + .feature { border-left: 1px solid var(--grey-line); }

  .sticky-bar {
    position: absolute; left: 0; top: 643px; width: 1067px; height: 125px;
    background: var(--white); box-shadow: 0 -2px 6px rgba(0,0,0,0.08);
  }
  .sticky-bar .brand { left: 14px; top: 38px; font-size: 20px; gap: 7px; }
  .sticky-bar .brand-mark { width: 14px; height: 14px; }
  .mini-features {
    position: absolute; left: 178px; top: 24px; height: 77px; display: flex;
  }
  .mini-feature {
    width: 147px; display: flex; flex-direction: column; align-items: center; justify-content: space-between;
    padding: 4px 0 2px; font-size: 15px; color: var(--grey-text); border-left: 1px solid var(--grey-line);
    white-space: nowrap;
  }
  .mini-feature.is-active { color: var(--cyan); }
  .mini-feature:last-child { border-right: 1px solid var(--grey-line); }
  .order-button {
    position: absolute; left: 919px; top: 37px; width: 130px; height: 61px;
    background: var(--cyan); color: var(--white); border-radius: 2px;
    display: flex; flex-direction: column; align-items: center; justify-content: center; line-height: 1.2;
  }
  .order-button .label { font-size: 18px; font-weight: 300; }
  .order-button .price { font-size: 21px; font-weight: 500; }

  .use-tabs {
    position: absolute; left: 0; top: 768px; width: 1067px; height: 39px;
    background: var(--tab-grey); display: flex; padding-left: 125px;
  }
  .use-tab {
    height: 39px; color: var(--white); font-size: 16px; display: flex; align-items: center; justify-content: center; position: relative;
  }
  .use-tab.is-active { background: var(--cyan); font-weight: 700; }
  .use-tab.is-active::after {
    content: ""; position: absolute; left: 50%; bottom: -13px; margin-left: -13px;
    border-left: 13px solid transparent; border-right: 13px solid transparent; border-top: 13px solid var(--cyan);
  }

  .use-slide { position: absolute; left: 0; top: 807px; width: 1067px; height: 393px; background: var(--white); }
  .slide-copy {
    position: absolute; left: 60px; top: 115px; width: 380px; text-align: center;
    font-style: italic; font-weight: 300; font-size: 24px; line-height: 1.3; color: var(--grey-text);
  }
  .use-slide .brand { left: 165px; top: 212px; font-size: 32px; }
  .use-slide .brand-mark { width: 22px; height: 22px; }
  .slide-photo-before {
    position: absolute; left: 448px; top: 40px; width: 228px; height: 353px;
    background: linear-gradient(180deg, #6d6d6d 0%, #bdbdbd 45%, #8a8a8a 100%);
  }
  .slide-photo-after {
    position: absolute; left: 676px; top: 40px; width: 321px; height: 353px;
    background: linear-gradient(180deg, #2b2630 0%, #6a3a48 35%, #2d63b0 70%, #8a8c90 100%);
  }
  .slide-dots { position: absolute; left: 181px; top: 361px; display: flex; gap: 13px; }
  .slide-dot { width: 14px; height: 14px; border-radius: 50%; background: #e2e2e2; }
  .slide-dot.is-active { background: var(--cyan); }
</style>
</head>
<body>

<header class="hero">
  <div class="brand"><span class="brand-mark"></span><span class="brand-name">FoldiPal-<br>Crate</span></div>
  <div class="tagline">fashionable , durable, multipurpose <strong>storage boxes</strong></div>

  <div class="product-shadow"></div>
  <div class="product-photo" role="img" aria-label="Blue folding storage box filled with groceries, fruit and drinks"></div>

  <svg class="chevron" style="left:257px;top:287px" width="32" height="64" viewBox="0 0 32 64"><polyline points="30,2 2,32 30,62" fill="none" stroke="#aaa" stroke-width="1.5"/></svg>
  <svg class="chevron" style="left:829px;top:287px" width="32" height="64" viewBox="0 0 32 64"><polyline points="2,2 30,32 2,62" fill="none" stroke="#aaa" stroke-width="1.5"/></svg>

  <ul class="features">
    <li class="feature">
      <svg width="40" height="36" viewBox="0 0 40 36"><rect x="4" y="14" width="32" height="10" rx="5" transform="rotate(-35 20 19)" fill="var(--grey-icon)"/><rect x="18" y="4" width="14" height="5" rx="2" transform="rotate(-35 25 6)" fill="var(--grey-icon)"/></svg>
      <span>Multipurpose</span>
    </li>
    <li class="feature">
      <svg width="34" height="36" viewBox="0 0 34 36"><rect x="3" y="2" width="28" height="30" fill="none" stroke="var(--grey-icon)" stroke-width="3"/><line x1="3" y1="12" x2="31" y2="12" stroke="var(--grey-icon)" stroke-width="3"/><line x1="3" y1="22" x2="31" y2="22" stroke="var(--grey-icon)" stroke-width="3"/><line x1="13" y1="7" x2="21" y2="7" stroke="var(--grey-icon)" stroke-width="2"/><line x1="13" y1="17" x2="21" y2="17" stroke="var(--grey-icon)" stroke-width="2"/><line x1="13" y1="27" x2="21" y2="27" stroke="var(--grey-icon)" stroke-width="2"/><line x1="5" y1="32" x2="5" y2="35" stroke="var(--grey-icon)" stroke-width="3"/><line x1="29" y1="32" x2="29" y2="35" stroke="var(--grey-icon)" stroke-width="3"/></svg>
      <span>Easy to store</span>
    </li>
    <li class="feature">
      <svg width="42" height="36" viewBox="0 0 42 36"><rect x="2" y="13" width="4" height="10" fill="var(--grey-icon)"/><rect x="7" y="8" width="6" height="20" fill="var(--grey-icon)"/><rect x="13" y="16" width="16" height="4" fill="var(--grey-icon)"/><rect x="29" y="8" width="6" height="20" fill="var(--grey-icon)"/><rect x="36" y="13" width="4" height="10" fill="var(--grey-icon)"/></svg>
      <span>Strong &amp; durable</span>
    </li>
    <li class="feature">
      <svg width="38" height="36" viewBox="0 0 38 36"><g fill="none" stroke="var(--grey-icon)" stroke-width="4"><path d="M13 10 L19 3 L25 12"/><path d="M30 17 L33 27 L22 29"/><path d="M14 29 L5 27 L9 17"/></g><g fill="var(--grey-icon)"><polygon points="22,13 30,13 27,6"/><polygon points="20,24 20,33 14,29"/><polygon points="5,14 12,12 10,20"/></g></svg>
      <span>100% Recyclable</span>
    </li>
    <li class="feature">
      <svg width="30" height="38" viewBox="0 0 30 38"><path d="M6 2 H18 V20 L26 28 Q29 32 26 34 H12 L10 27 L8 36 H5 L6 22 Z" fill="var(--grey-icon)"/></svg>
      <span>5 Unique Styles</span>
    </li>
  </ul>
</header>

<nav class="sticky-bar">
  <div class="brand"><span class="brand-mark"></span><span class="brand-name">FoldiPal-<br>Crate</span></div>
  <ul class="mini-features">
    <li class="mini-feature is-active">
      <svg width="32" height="30" viewBox="0 0 40 36"><rect x="4" y="14" width="32" height="10" rx="5" transform="rotate(-35 20 19)" fill="var(--cyan)"/><rect x="18" y="4" width="14" height="5" rx="2" transform="rotate(-35 25 6)" fill="var(--cyan)"/></svg>
      <span>Multipurpose</span>
    </li>
    <li class="mini-feature">
      <svg width="28" height="30" viewBox="0 0 34 36"><rect x="3" y="2" width="28" height="30" fill="none" stroke="var(--grey-icon)" stroke-width="3"/><line x1="3" y1="12" x2="31" y2="12" stroke="var(--grey-icon)" stroke-width="3"/><line x1="3" y1="22" x2="31" y2="22" stroke="var(--grey-icon)" stroke-width="3"/><line x1="13" y1="7" x2="21" y2="7" stroke="var(--grey-icon)" stroke-width="2"/><line x1="13" y1="17" x2="21" y2="17" stroke="var(--grey-icon)" stroke-width="2"/><line x1="13" y1="27" x2="21" y2="27" stroke="var(--grey-icon)" stroke-width="2"/></svg>
      <span>Easy to store</span>
    </li>
    <li class="mini-feature">
      <svg width="36" height="30" viewBox="0 0 42 36"><rect x="2" y="13" width="4" height="10" fill="var(--grey-icon)"/><rect x="7" y="8" width="6" height="20" fill="var(--grey-icon)"/><rect x="13" y="16" width="16" height="4" fill="var(--grey-icon)"/><rect x="29" y="8" width="6" height="20" fill="var(--grey-icon)"/><rect x="36" y="13" width="4" height="10" fill="var(--grey-icon)"/></svg>
      <span>Strong &amp; durable</span>
    </li>
    <li class="mini-feature">
      <svg width="32" height="30" viewBox="0 0 38 36"><g fill="none" stroke="var(--grey-icon)" stroke-width="4"><path d="M13 10 L19 3 L25 12"/><path d="M30 17 L33 27 L22 29"/><path d="M14 29 L5 27 L9 17"/></g><g fill="var(--grey-icon)"><polygon points="22,13 30,13 27,6"/><polygon points="20,24 20,33 14,29"/><polygon points="5,14 12,12 10,20"/></g></svg>
      <span>100% Recyclable</span>
    </li>
    <li class="mini-feature">
      <svg width="26" height="32" viewBox="0 0 30 38"><path d="M6 2 H18 V20 L26 28 Q29 32 26 34 H12 L10 27 L8 36 H5 L6 22 Z" fill="var(--grey-icon)"/></svg>
      <span>5 Unique Styles</span>
    </li>
  </ul>
  <div class="order-button"><span class="label">Order now</span><span class="price">£14.99</span></div>
</nav>

<ul class="use-tabs">
  <li class="use-tab is-active" style="width:132px">Shopping</li>
  <li class="use-tab" style="width:124px">Laundry</li>
  <li class="use-tab" style="width:128px">Camping</li>
  <li class="use-tab" style="width:124px">Gardening</li>
  <li class="use-tab" style="width:128px">Moving</li>
  <li class="use-tab" style="width:116px">Office</li>
  <li class="use-tab" style="width:128px">Play room</li>
</ul>

<section class="use-slide">
  <svg class="chevron" style="left:11px;top:200px" width="30" height="60" viewBox="0 0 30 60"><polyline points="28,2 2,30 28,58" fill="none" stroke="#aaa" stroke-width="1.5"/></svg>
  <p class="slide-copy">Don’t struggle with conventional plastic bags for shopping, use</p>
  <div class="brand"><span class="brand-mark"></span><span class="brand-name">FoldiPal-<br>Crate</span></div>
  <div class="slide-photo-before" role="img" aria-label="Black and white photo of a shopper struggling with many plastic carrier bags"></div>
  <div class="slide-photo-after" role="img" aria-label="Colour photo of a smiling shopper carrying a full blue folding crate in a supermarket"></div>
  <svg class="chevron" style="left:1027px;top:200px" width="30" height="60" viewBox="0 0 30 60"><polyline points="2,2 28,30 2,58" fill="none" stroke="#aaa" stroke-width="1.5"/></svg>
  <div class="slide-dots">
    <span class="slide-dot is-active"></span><span class="slide-dot"></span><span class="slide-dot"></span><span class="slide-dot"></span><span class="slide-dot"></span>
  </div>
</section>

</body>
</html>
```